Watch brand needs new business cards

Kestrel Timepiece Company are looking for a new business card design incorporating our logo and brand colours as per our website.

Design should be 90x55mm with 3mm print margin from edges and 3mm external bleed.

Card should be double sided, e.g. logo one side, personal details on the other.

Logo will be provided as a vector.

The card must be able to show:
- Staff name
- Position
- Office Address
- Email
- Telephone number
- Website address

Final work must be provided in an editable format to allow us to add staff details (e.g. an AI or PSD file).

```html
<!DOCTYPE html>
<html lang="en">
<head>
<meta charset="utf-8">
<title>Kestrel Timepiece Company – Business Cards</title>
<link rel="stylesheet" href="https://fonts.googleapis.com/css2?family=Exo+2:wght@600&family=Roboto:wght@400;500&display=swap">
<style>
  :root {
    --backdrop: #e4e4e4;
    --card-dark: #1f1b1b;
    --card-light: #f4f4f4;
    --band-grey: #4a4a4a;
    --ink: #1a1a1a;
    --silver: #dcdcdc;
    --white: #ffffff;
  }
  * { margin: 0; padding: 0; box-sizing: border-box; }
  html, body { width: 1200px; height: 576px; overflow: hidden; background: var(--backdrop); }
  body { position: relative; font-family: "Roboto", Arial, sans-serif; }

  .card { position: absolute; width: 482px; height: 292px; border-radius: 6px; overflow: hidden; }
  .card--front { left: 82px; top: 139px; background: var(--card-dark); }
  .card--back { left: 602px; top: 138px; background: var(--card-light); }

  .brand { position: absolute; display: flex; flex-direction: column; align-items: center; transform: translateX(-50%); }
  .brand__ring { border-radius: 50%; border: 3px solid currentColor; }
  .brand__name { font-family: "Roboto", Arial, sans-serif; font-weight: 500; white-space: nowrap; }

  .card--front .brand { left: 241px; top: 78px; color: var(--silver); }
  .card--front .brand__ring { width: 70px; height: 70px; }
  .card--front .brand__name { font-size: 25px; margin-top: 22px; }

  .card--back .brand { left: 132px; top: 68px; color: var(--ink); }
  .card--back .brand__ring { width: 90px; height: 90px; border-width: 4px; }
  .card--back .brand__name { font-size: 18px; margin-top: 22px; }

  .wave { position: absolute; left: 0; top: 0; width: 482px; height: 292px; }
  .wave__dark { fill: var(--card-dark); }
  .wave__band { fill: var(--band-grey); }

  .person { position: absolute; right: 24px; top: 30px; text-align: right; color: var(--white); }
  .person__name { font-family: "Exo 2", Arial, sans-serif; font-weight: 600; font-size: 19px; letter-spacing: 0.3px; }
  .person__role { font-size: 11px; margin-top: 4px; }

  .address { position: absolute; left: 30px; top: 236px; font-size: 13px; line-height: 18px; color: var(--ink); font-style: normal; }

  .contacts { position: absolute; left: 268px; top: 214px; list-style: none; font-size: 13px; color: var(--ink); }
  .contacts li { display: flex; align-items: center; height: 18.5px; }
  .contacts svg { width: 10px; height: 10px; margin-right: 8px; fill: var(--ink); flex: none; }
</style>
</head>
<body>

<section class="card card--front" aria-label="Card front">
  <div class="brand">
    <span class="brand__ring"></span>
    <span class="brand__name">Kestrel Timepiece Company</span>
  </div>
</section>

<section class="card card--back" aria-label="Card back">
  <svg class="wave" viewBox="0 0 600 365" preserveAspectRatio="none" aria-hidden="true">
    <path class="wave__dark" d="M0 0 H600 V132 C500 126 420 72 300 40 C190 12 80 16 0 42 Z"/>
    <path class="wave__band" d="M0 54 C80 30 190 24 300 52 C420 84 500 142 600 152 V172 C500 164 420 104 300 72 C190 44 80 46 0 76 Z"/>
  </svg>

  <div class="person">
    <div class="person__name">Daniel Hart</div>
    <div class="person__role">Managing Director</div>
  </div>

  <div class="brand">
    <span class="brand__ring"></span>
    <span class="brand__name">Kestrel Timepiece Company</span>
  </div>

  <address class="address">418 Larkspur Avenue<br>Fairhaven Oregon 97000</address>

  <ul class="contacts">
    <li>
      <svg viewBox="0 0 10 10" aria-hidden="true"><path d="M1 3 C1 1.5 3 1 5 1 C7 1 9 1.5 9 3 L7.5 3.6 L7 2.6 H3 L2.5 3.6 Z M2.5 4.5 H7.5 L8.5 9 H1.5 Z"/></svg>
      +1 555 014 2290
    </li>
    <li>
      <svg viewBox="0 0 10 10" aria-hidden="true"><circle cx="5" cy="5" r="4.3" fill="none" stroke="#1a1a1a" stroke-width="1"/><ellipse cx="5" cy="5" rx="1.8" ry="4.3" fill="none" stroke="#1a1a1a" stroke-width="0.9"/><path d="M0.8 5 H9.2" stroke="#1a1a1a" stroke-width="0.9"/></svg>
      www.kestreltimepiece.com
    </li>
    <li>
      <svg viewBox="0 0 10 10" aria-hidden="true"><path d="M0.5 2 H9.5 V8.5 H0.5 Z" /><path d="M0.5 2 L5 5.8 L9.5 2" fill="none" stroke="#f4f4f4" stroke-width="0.9"/></svg>
      daniel@kestreltimepiece.com
    </li>
  </ul>
</section>

</body>
</html>
```